Placing my newer logo on my existing business card

I have a business card that I had you guys do years ago, then I changed my logo, I love both my business card and my logo. The challenge is both my logo and my business card are very similar in color. So I'm not sure how to make my logo stand out.

Sick

```html
<!DOCTYPE html>
<html lang="en">
<head>
<meta charset="utf-8">
<title>Alder Ridge Wellness – Card Set</title>
<link rel="stylesheet" href="https://fonts.googleapis.com/css2?family=Tinos:wght@400;700&family=Great+Vibes&display=swap">
<style>
  :root {
    --ink: #111;
    --brand-ink: #3b2a26;
    --rust: #b5532f;
    --rust-soft: #c98a5e;
    --sky-top: #ffffff;
    --sky-mid: #bfe2f3;
    --sky-deep: #74c4e8;
    --copper: #b0602f;
    --copper-light: #d9a48a;
    --maroon: #56121a;
    --bullet: #7a78b8;
    --text-font: "Tinos", "Times New Roman", serif;
    --script-font: "Great Vibes", cursive;
  }
  * { box-sizing: border-box; margin: 0; padding: 0; }
  html, body { width: 1200px; height: 800px; overflow: hidden; background: #fff; }
  body { position: relative; font-family: var(--text-font); color: var(--ink); }

  .card { position: absolute; width: 506px; height: 296px; overflow: hidden; }
  .card--profile { left: 44px; top: 57px; background: linear-gradient(180deg, var(--sky-top) 0%, var(--sky-mid) 55%, var(--sky-deep) 100%); }
  .card--contact { left: 640px; top: 57px; background: linear-gradient(180deg, var(--sky-top) 0%, #bfe3f3 50%, #8fd0ec 100%); }
  .card--services { left: 47px; top: 440px; background: linear-gradient(180deg, #92d2ec 0%, #c5e6f4 50%, #ffffff 100%); }
  .card--appointment { left: 640px; top: 440px; background: linear-gradient(180deg, var(--copper) 0%, var(--copper-light) 48%, #8a3a28 75%, var(--maroon) 100%); }

  .abs { position: absolute; }
  .center-text { text-align: center; }

  .brand { display: flex; align-items: center; justify-content: center; gap: 8px; color: var(--brand-ink); font-family: var(--text-font); font-weight: 700; white-space: nowrap; line-height: 1; }
  .brand__dot { width: 0.6em; height: 0.6em; border-radius: 50%; background: var(--brand-ink); flex: none; }

  /* profile card */
  .profile__brand { left: 0; width: 326px; top: 66px; font-size: 21px; }
  .profile__name { left: 0; width: 326px; top: 130px; font-size: 23px; font-weight: 700; }
  .profile__role { left: 0; width: 326px; top: 157px; font-size: 12px; color: var(--rust-soft); }
  .profile__details { left: 0; width: 326px; top: 184px; font-size: 13.5px; line-height: 17.5px; }
  .profile__details p + p { margin-top: 10px; }
  .profile__photo { right: 0; top: 0; width: 200px; height: 296px;
    background: linear-gradient(90deg, rgba(255,255,255,0) 0%, rgba(230,215,200,0.9) 25%, #d9bfa5 55%, #c9a585 100%); }

  /* contact card */
  .contact__brand { left: 40px; width: 300px; top: 106px; font-size: 26px; }
  .contact__lines { left: 40px; width: 300px; top: 160px; font-size: 15px; line-height: 22px; }
  .contact__lines .label { color: var(--rust); }
  .contact__divider { left: 57px; top: 209px; }
  .contact__address { left: 40px; width: 300px; top: 222px; font-size: 14.5px; line-height: 20px; }
  .contact__band { right: 0; top: 0; }

  /* services card */
  .services__title { left: 0; width: 506px; top: 18px; font-size: 15.5px; font-weight: 700; }
  .services__list { list-style: none; font-size: 12px; line-height: 16px; }
  .services__list li { position: relative; padding-left: 15px; }
  .services__list li::before { content: ""; position: absolute; left: 0; top: 4px; width: 7px; height: 7px; border-radius: 50%; background: var(--bullet); }
  .services__list--left { left: 40px; top: 41px; }
  .services__list--right { left: 301px; top: 41px; }
  .services__rule { left: 40px; top: 222px; width: 428px; height: 1px; background: var(--ink); }
  .services__brand { left: 40px; top: 236px; font-size: 15px; justify-content: flex-start; }
  .services__call { right: 38px; top: 229px; font-size: 20px; text-align: right; }
  .services__web { right: 38px; top: 256px; font-size: 12px; text-align: right; }
  .services__flourish { right: 0; top: 0; width: 130px; height: 296px;
    background: linear-gradient(90deg, rgba(255,255,255,0) 0%, rgba(214,190,175,0.35) 45%, rgba(255,255,255,0) 100%); }

  /* appointment card */
  .appointment__panel { left: 26px; top: 23px; width: 454px; height: 250px;
    background: linear-gradient(180deg, #ffffff 0%, #d9eef8 45%, #9dd5ee 100%); }
  .appointment__flourish { right: 20px; top: 0; width: 110px; height: 296px;
    background: linear-gradient(90deg, rgba(255,255,255,0) 0%, rgba(200,190,185,0.35) 50%, rgba(255,255,255,0) 100%); }
  .appointment__brand { left: 0; width: 506px; top: 46px; font-size: 18px; }
  .appointment__heading { left: 0; width: 506px; top: 94px; font-size: 13px; letter-spacing: 0.2em; }
  .appointment__field { top: 162px; font-size: 13px; }
  .appointment__line { top: 174px; height: 1px; background: var(--ink); }
  .appointment__tagline { left: 0; width: 506px; top: 228px; font-family: var(--script-font); font-size: 30px; }
</style>
</head>
<body>

  <section class="card card--profile">
    <div class="abs profile__photo" role="img" aria-label="Portrait photo of the director in a white coat against a brick wall"></div>
    <div class="abs brand profile__brand"><span class="brand__dot"></span><span>Alder Ridge Wellness</span></div>
    <h1 class="abs center-text profile__name">Marla Jennings</h1>
    <p class="abs center-text profile__role">Director</p>
    <div class="abs center-text profile__details">
      <p>1450 Ridge Ave ste#2<br>Millbrook Utah 84000</p>
      <p>1(555)214-7730<br>www.alderridgewellness.com</p>
    </div>
  </section>

  <section class="card card--contact">
    <svg class="abs contact__band" width="170" height="296" viewBox="0 0 170 296" aria-hidden="true">
      <defs>
        <linearGradient id="bandFill" x1="0" y1="0" x2="0" y2="1">
          <stop offset="0" stop-color="#b0602f"/>
          <stop offset="0.35" stop-color="#d49a80"/>
          <stop offset="0.7" stop-color="#7a2a22"/>
          <stop offset="1" stop-color="#56121a"/>
        </linearGradient>
      </defs>
      <path d="M60 0 C110 40 100 110 55 160 C20 200 40 250 70 296 L170 296 L170 0 Z" fill="url(#bandFill)"/>
    </svg>
    <div class="abs brand contact__brand"><span class="brand__dot"></span><span>Alder Ridge Wellness</span></div>
    <div class="abs center-text contact__lines">
      <p><span class="label">PH</span>: (555) 214-7730 &nbsp;| &nbsp;<span class="label">FX</span>: (555) 214-7731</p>
      <p>alderridgewellness.com</p>
    </div>
    <svg class="abs contact__divider" width="260" height="8" viewBox="0 0 260 8" aria-hidden="true">
      <line x1="0" y1="4" x2="260" y2="4" stroke="#333" stroke-width="0.8"/>
      <circle cx="130" cy="4" r="3" fill="#111"/>
    </svg>
    <div class="abs center-text contact__address">
      <p>1450 ridge ave ste#2</p>
      <p>millbrook ut 84000</p>
    </div>
  </section>

  <section class="card card--services">
    <div class="abs services__flourish" role="img" aria-label="Faint decorative swirl ribbon"></div>
    <h2 class="abs center-text services__title">Conditions we address for women and men</h2>
    <ul class="abs services__list services__list--left">
      <li>PCOS</li><li>Hysterectomy</li><li>Type-II Diabetes</li><li>Insulin Resistance</li>
      <li>Hypothyroid</li><li>Underactive Thyroid</li><li>Fibromyalgia</li><li>Chronic Fatigue</li>
      <li>Chronic Headaches &amp; Migraines</li><li>Hypertension</li><li>Elevated Fasting Glucose</li>
    </ul>
    <ul class="abs services__list services__list--right">
      <li>Pre-Diabetes</li><li>Abdominal Obesity</li><li>High Triglycerides</li><li>High Blood Pressure</li>
      <li>High Cholesterol</li><li>Gestational Diabetes</li><li>Epstein Bar</li><li>Infertility</li>
      <li>Infertility Drugs</li><li>Anti-Depression Medications</li>
    </ul>
    <div class="abs services__rule"></div>
    <div class="abs brand services__brand"><span class="brand__dot"></span><span>Alder Ridge Wellness</span></div>
    <p class="abs services__call">Call Today!: (555)214-7730</p>
    <p class="abs services__web">www.alderridgewellness.com</p>
  </section>

  <section class="card card--appointment">
    <div class="abs appointment__panel"></div>
    <div class="abs appointment__flourish" role="img" aria-label="Faint decorative swirl ribbon"></div>
    <div class="abs brand appointment__brand"><span class="brand__dot"></span><span>Alder Ridge Wellness</span></div>
    <p class="abs center-text appointment__heading">APPOINTMENT ON....</p>
    <span class="abs appointment__field" style="left:42px">Time</span>
    <span class="abs appointment__line" style="left:76px; width:155px"></span>
    <span class="abs appointment__field" style="left:239px">Date</span>
    <span class="abs appointment__line" style="left:271px; width:192px"></span>
    <p class="abs center-text appointment__tagline">Let's Make it Happen</p>
  </section>

</body>
</html>
```